business card template & company stationery
for Blue Pine Device Wizard - Computer Support
business card template & company stationery -
Creative Brief
Bright & Fun-filled
Dale Harwick
Service Manager
47 E. Birch Ave. (Rt. 58) Alden, VT 02519
dale@bluepinedevicewizard.com
www.BluePineDeviceWizard.com
I will upload the logo info shortly. The phone number is the most important contact info for us.
On the back of the card I was planning to have either a solid blue or orange background with our logo centered in all white, but I'm open to other ideas. The white on blue and orange versions are included with the logos

```html
<!DOCTYPE html>
<html lang="en">
<head>
<meta charset="utf-8">
<title>Blue Pine Device Wizard – Business Card</title>
<link href="https://fonts.googleapis.com/css2?family=Open+Sans:wght@400;600;700&display=swap" rel="stylesheet">
<style>
  :root {
    --backdrop: #2b2b2d;
    --card: #f7f7f7;
    --orange: #f08a1c;
    --blue: #2f7fc1;
    --ink: #3a3a3a;
    --ink-soft: #5a5a5a;
  }
  * { margin: 0; padding: 0; box-sizing: border-box; }
  html, body { width: 1200px; height: 845px; overflow: hidden; }
  body {
    background: var(--backdrop);
    font-family: "Open Sans", Arial, sans-serif;
    position: relative;
  }
  .card {
    position: absolute;
    width: 518px;
    height: 298px;
    border-radius: 20px;
    background: linear-gradient(180deg, #ffffff 0%, var(--card) 60%, #ececec 100%);
    box-shadow: 0 6px 18px rgba(0,0,0,0.45);
  }
  .card--front { left: 149px; top: 84px; }
  .card--back  { left: 526px; top: 424px; }

  /* brand line */
  .brand {
    position: absolute;
    display: flex;
    align-items: center;
    gap: 14px;
  }
  .brand__mark { background: var(--orange); flex: none; }
  .brand__name {
    font-weight: 600;
    color: var(--ink);
    letter-spacing: -0.3px;
    white-space: nowrap;
  }

  /* front */
  .brand--front { left: 80px; top: 132px; }
  .brand--front .brand__mark { width: 26px; height: 26px; }
  .brand--front .brand__name { font-size: 26px; }

  .holder {
    position: absolute;
    right: 42px;
    top: 212px;
  }
  .holder__name {
    font-weight: 700;
    font-size: 17px;
    color: var(--orange);
  }
  .holder__role {
    font-size: 11px;
    color: var(--ink);
    margin-top: 2px;
  }

  /* back */
  .brand--back {
    right: 36px;
    top: 92px;
    flex-direction: column;
    align-items: flex-end;
    gap: 10px;
  }
  .brand--back .brand__mark { width: 40px; height: 40px; }
  .brand--back .brand__name { font-size: 17px; }

  .contacts {
    position: absolute;
    left: 30px;
    top: 134px;
    list-style: none;
  }
  .contacts li {
    display: flex;
    align-items: flex-start;
    gap: 22px;
    font-size: 11px;
    line-height: 14px;
    color: var(--ink-soft);
    margin-bottom: 10px;
    white-space: nowrap;
  }
  .contacts li.address { margin-bottom: 12px; }
  .contacts svg { width: 14px; height: 14px; flex: none; fill: var(--orange); }
</style>
</head>
<body>

  <section class="card card--front">
    <div class="brand brand--front">
      <span class="brand__mark"></span>
      <span class="brand__name">Blue Pine Device Wizard</span>
    </div>
    <div class="holder">
      <p class="holder__name">Dale Harwick</p>
      <p class="holder__role">Service Manager</p>
    </div>
  </section>

  <section class="card card--back">
    <div class="brand brand--back">
      <span class="brand__mark"></span>
      <span class="brand__name">Blue Pine Device Wizard</span>
    </div>
    <ul class="contacts">
      <li class="address">
        <svg viewBox="0 0 16 16" aria-hidden="true"><path d="M8 1 1 7.5h2V15h4v-4h2v4h4V7.5h2z"/></svg>
        <span>47 E. Birch Ave. (Rt. 58)<br>Alden, VT 02519</span>
      </li>
      <li>
        <svg viewBox="0 0 16 16" aria-hidden="true"><path d="M3 1h3l1.5 4-2 1.3a9 9 0 0 0 4.2 4.2L11 8.5l4 1.5v3a2 2 0 0 1-2 2A12 12 0 0 1 1 3a2 2 0 0 1 2-2z"/></svg>
        <span>(413) 555-0148</span>
      </li>
      <li>
        <svg viewBox="0 0 16 16" aria-hidden="true"><path d="M4 1h7l2 2v3H4zM1 7h14v7H1zm3 2v2h8V9z"/></svg>
        <span>(877) 555-0193</span>
      </li>
      <li>
        <svg viewBox="0 0 16 16" aria-hidden="true"><path d="M8 1a7 7 0 1 0 3.5 13l-.7-1.3A5.5 5.5 0 1 1 13.5 8v.8c0 .8-.5 1.3-1.1 1.3s-1-.5-1-1.3V4.5H10v.6A3.4 3.4 0 1 0 10.3 11a2.5 2.5 0 0 0 2.1 1.1c1.5 0 2.6-1.2 2.6-3.3V8A7 7 0 0 0 8 1zm-.2 4.7a2 2 0 1 1 0 4.6 2 2 0 0 1 0-4.6z"/></svg>
        <span>dale@bluepinedevicewizard.com</span>
      </li>
      <li>
        <svg viewBox="0 0 16 16" aria-hidden="true"><path d="M8 1a7 7 0 1 0 0 14A7 7 0 0 0 8 1zm0 1.5c.8.8 1.5 2.3 1.7 4.5H6.3C6.5 4.8 7.2 3.3 8 2.5zM2.6 7h2.2c.1-1.7.5-3.1 1.1-4.1A5.5 5.5 0 0 0 2.6 7zm0 2a5.5 5.5 0 0 0 3.3 4.1C5.3 12.1 4.9 10.7 4.8 9zm3.7 0h3.4c-.2 2.2-.9 3.7-1.7 4.5-.8-.8-1.500-2.3-1.7-4.5zm4.9 0h2.2a5.5 5.5 0 0 1-3.3 4.1c.6-1 1-2.4 1.1-4.1zm2.2-2h-2.2c-.1-1.7-.5-3.1-1.1-4.1A5.5 5.5 0 0 1 13.4 7z"/></svg>
        <span>www.BluePineDeviceWizard.com</span>
      </li>
    </ul>
  </section>

</body>
</html>
```